Trifold A4 doublesided flyer/brochure and possibly logo redisgn for Qorvel Vending solutions

We are a Sydney based drink and snack vending machine company that supply maintain and restock free vending machines for Sydney businesses. Most our sites are office work places as well as some training organizations and a gym. We require a Trifold A4 double sided flyer/brochure we can letterbox drop to local businesses that have a large amount of staff and would benefit from a vending machine in there staff lunchroom. We would also like to use the flyer for larger businesses that may have a showroom for there own customers.
The flyer needs to look sophisticated modern and professional and immediately convey the offer of a fully installed serviced and maintained vending machine absolutely FREE.
Also needs to include
Vending machine features
Our large range of products especially healthy options
Our ongoing support and servicing and commitment to superior service
We essentially dont have a logo so some sort of logo design would be a bonus
I am trying to look for high quality pictures suitable for print but i am finding it difficult.
I will keep searching and post soon.
We would like the original document or the general background as well so we can modify or add new text later our self resend a different version of the flyer
Our website has some pictures but they are not good enough for print.
www.qorvelindustries.com.au
We can use the main elements form the website but does not need to look the same or use the same fonts. you can give any thing a try although it would be good to tie in

Requirements
Must have
• I have uploaded a word document with some content and some pictures.
Pictures can be used at your discretion. you dont have to use these

```html
<!DOCTYPE html>
<html lang="en">
<head>
<meta charset="utf-8">
<title>Qorvel Vending Solutions – Trifold Brochure</title>
<link rel="stylesheet" href="https://fonts.googleapis.com/css2?family=Lustria&family=Noto+Serif:wght@400;700&display=swap">
<style>
  :root{
    --blue:#0a6fd0;
    --blue-bright:#1a8ae6;
    --blue-deep:#0a4fa0;
    --navy:#0d3a7a;
    --black:#000;
    --charcoal:#111214;
    --graphite:#2a2b2e;
    --white:#fff;
    --red:#e4252b;
  }
  *{margin:0;padding:0;box-sizing:border-box}
  html,body{width:846px;height:1200px;overflow:hidden;background:var(--white)}
  body{font-family:"Lustria","Noto Serif",serif;color:var(--white);position:relative}
  .panel{position:absolute;overflow:hidden}
  .waves{position:absolute;left:0;top:380px;width:846px;height:220px;pointer-events:none}

  /* outside spread */
  .intro{left:0;top:0;width:282px;height:598px;background:linear-gradient(180deg,#0b74d6 0%,#0a6acb 60%,#0a5fb8 100%)}
  .intro p{position:absolute;left:20px;width:241px;font-size:12.2px;line-height:17.4px;text-align:justify;letter-spacing:.55px}
  .hl{color:var(--red)}
  .contact{left:282px;top:0;width:281px;height:598px;background:linear-gradient(180deg,#000 0%,#000 65%,#071a33 100%)}
  .contact .lead{position:absolute;left:16px;top:30px;width:252px;font-size:13.6px;line-height:21px;letter-spacing:.7px}
  .contact dl{position:absolute;left:16px;top:136px;font-size:13.6px;line-height:21px;display:grid;grid-template-columns:66px auto;letter-spacing:.4px}
  .contact .web-lead{position:absolute;left:16px;top:238px;font-size:13.6px;letter-spacing:.5px}
  .contact .web{position:absolute;left:16px;top:280px;font-size:13.6px;letter-spacing:.5px}
  .ghost-name{position:absolute;left:0;width:281px;top:462px;text-align:center;font-size:22px;line-height:26px;color:rgba(40,110,200,.55)}
  .cover{left:563px;top:0;width:283px;height:598px;background:linear-gradient(180deg,#fff 0%,#fff 62%,#e6eef8 100%)}
  .brand{position:absolute;left:0;top:108px;width:283px;text-align:center;color:var(--navy);font-size:34px;line-height:40px;font-weight:400}
  .brand .mark{display:block;width:22px;height:22px;background:var(--navy);margin:0 auto 10px}
  .tagline{position:absolute;left:0;top:286px;width:283px;height:101px;background:linear-gradient(180deg,var(--blue-bright),var(--blue));display:block;padding-top:21px;text-align:center;font-size:19px;line-height:29px}

  .fold-gap{position:absolute;left:0;top:598px;width:846px;height:4px;background:var(--white)}

  /* inside spread */
  .machines{left:0;top:602px;width:282px;height:598px;background:var(--black)}
  .machines p{position:absolute;left:22px;top:44px;width:240px;font-size:12.2px;line-height:17.2px;text-align:justify;letter-spacing:.55px}
  .machine-photo{position:absolute;left:8px;top:394px;width:264px;height:204px;background:linear-gradient(180deg,#d9dde2,#8e959e 55%,#2c2f33)}
  .services{left:282px;top:602px;width:281px;height:598px;background:linear-gradient(180deg,#1d1e20,#0e0f10)}
  .services h3{position:absolute;left:11px;font-family:"Noto Serif",serif;font-weight:700;font-size:11.4px}
  .services p{position:absolute;left:11px;width:255px;font-size:6.6px;line-height:9.6px;text-align:justify;text-indent:10px;letter-spacing:.15px}
  .products{left:563px;top:602px;width:283px;height:598px;background:var(--graphite)}
  .snack-photo{position:absolute;left:12px;top:8px;width:260px;height:272px;background:linear-gradient(135deg,#c3262a,#e59b2a 35%,#5a3b8e 60%,#2b6fc0 80%,#e6e0d8);border:1px solid #555}
  .products p{position:absolute;left:24px;top:438px;width:238px;font-size:10.1px;line-height:15.2px;text-align:justify;letter-spacing:.45px}

  .band{position:absolute;left:0;top:858px;width:846px;height:182px;pointer-events:none}
  .band-title{position:absolute;font-size:29px;font-weight:400;color:var(--white);line-height:1}
  .t-machines{left:9px;top:897px}
  .t-services{left:354px;top:929px}
  .t-products{left:653px;top:955px}
</style>
</head>
<body>

<!-- outside spread -->
<section class="panel intro">
  <p style="top:113px">Qorvel Vending solutions specializes in giving FREE Vending Machines to all types of businesses in Sydney and the surrounding suburbs. We can install a vending machine in your workplace that we stock, manage, maintain, service and support, at absolutely <span class="hl">no cost</span> to you, <span class="hl">EVER</span>!</p>
  <p style="top:268px">We take all the hassles and headaches out of having a vending machine at your venue so you can focus on what is truly important. We only stock the highest quality product range that is tailored to your needs including healthy and gluten free options. Simply APPLY NOW or contact us to have a FREE Vending machine installed at your work place today.</p>
</section>

<section class="panel contact">
  <p class="lead">For more information, or to request a free Vending Machine, feel free to contact us 24 hours a day 7 days a week!</p>
  <dl>
    <dt>Phone :</dt><dd>1300 472 09</dd>
    <dt>Mobile:</dt><dd>0400 555 210</dd>
    <dt>Email:</dt><dd>info.desk@qorvelmail.com</dd>
    <dt>Email:</dt><dd>office.qv@qorvelmail.com</dd>
  </dl>
  <p class="web-lead">Or visit us on the web at:</p>
  <p class="web">www.qorvelindustries.com.au</p>
  <p class="ghost-name">Qorvel<br>Vending<br>Solutions</p>
</section>

<section class="panel cover">
  <h1 class="brand"><span class="mark"></span>Qorvel<br>Vending<br>Solutions</h1>
  <p class="tagline">Your source for&nbsp; 100% <span class="hl">FREE</span><br>Vending Machines!</p>
</section>

<svg class="waves" viewBox="0 0 846 220" aria-hidden="true">
  <g fill="none" stroke-linecap="round">
    <path d="M0 95 C150 60 300 150 846 90" stroke="rgba(255,255,255,.55)" stroke-width="2"/>
    <path d="M0 110 C160 80 320 170 846 105" stroke="rgba(120,190,255,.6)" stroke-width="1.5"/>
    <path d="M0 125 C170 95 340 185 846 118" stroke="rgba(40,120,230,.7)" stroke-width="3"/>
    <path d="M0 140 C180 120 360 200 846 135" stroke="rgba(255,255,255,.35)" stroke-width="1"/>
    <path d="M0 75 C140 50 300 130 846 70" stroke="rgba(90,160,240,.45)" stroke-width="1"/>
  </g>
</svg>

<div class="fold-gap"></div>

<!-- inside spread -->
<section class="panel machines">
  <p>Qorvel Vending has a large range of machines to choose from which enables us to tailor a package for any situation. Our preferred machines are manufactured in Italy and have proven to be the most reliable machines available. They are among the most modern and technologically advanced machines available today and come in a wide choice of sizes and configurations.</p>
  <div class="machine-photo" role="img" aria-label="Row of glass-front snack and drink vending machines"></div>
</section>

<section class="panel services">
  <h3 style="top:19px">Sydneys Leading Vending Company</h3>
  <p style="top:38px">Qorvel vending solutions is Sydney's premier vending company. Our goal is to provide an unmatched service with reliable machines, great products and 24hr support. Only supplying the greater Sydney area enables us to have an extremely personalize service and quick and efficient 24hr support. Our focus is on customer satisfaction and we strive for excellence in our field. We only use the best products with Italian made vending machines that have been proven to be the most reliable and highest quality available.</p>
  <h3 style="top:135px">Customized Vending Solutions</h3>
  <p style="top:154px">Qorvel tailor a unique vending solution for each of our clients either large or small. Clients are able to chose there own range from our large product inventory or even request new items at any time, or alternatively we can design a vending machine product package that will best suit your demographic. We continually strive to improve our service and understand that one size does not fit all. We know different products meet the requirements of different people even at different times and this is why we continually monitor your selections and adjust stock to your needs.</p>
  <h3 style="top:415px">24 Hour Support</h3>
  <p style="top:434px">Qorvel Vending solutions is on hand 24 hours a day to provide ongoing support should the unlikely event of a coin jam or maintenance issue arise. Our qualified technicians are on call and will immediately respond to any call outs absolutely free of charge. All our machines are regularly tested and serviced to ensure ongoing reliability and seamless operation.</p>
  <h3 style="top:509px">Regular Stocking and Servicing</h3>
  <p style="top:528px">Qorvel Vending provides trained technicians to regularly service and restock machines ensuring they are always stocked with the latest products. They will closely monitor your selections and suggest new products based on current sales keeping our service extremely personalized and providing great product variety.</p>
</section>

<section class="panel products">
  <div class="snack-photo" role="img" aria-label="Heap of assorted chocolate bars, chips and snack packets"></div>
  <p>Qorvel Vending solutions stock an extremely large range of high quality products that are tailored to individual needs. We have many numerous existing clients including industrial centers, offices, shops, schools/training centers, gyms and even health clubs. Such a varied customer base requires a diverse and extensive range of products to choose from. We work with our clients to ensure products are suitable and consistently up to date.</p>
</section>

<svg class="band" viewBox="0 0 846 182" aria-hidden="true">
  <defs>
    <linearGradient id="bandFill" x1="0" y1="0" x2="0" y2="1">
      <stop offset="0" stop-color="#1a8ae6"/>
      <stop offset="1" stop-color="#0a62c4"/>
    </linearGradient>
  </defs>
  <path d="M0 30 H100 L130 0 L160 30 H298 L328 0 L358 30 H846 V132 H740 L710 162 L680 132 H548 L518 162 L488 132 H0 Z" fill="url(#bandFill)"/>
</svg>
<h2 class="band-title t-machines">Vending Machines</h2>
<h2 class="band-title t-services">Services</h2>
<h2 class="band-title t-products">Products</h2>

</body>
</html>
```